Lumo Cellar Traders needs a new business card design

Colour theme: Gold + Red preferred
Front side: Main logo with my details as below;
Back side: Theme of some wine glasses or bottles, maybe different color of log together
Lumo Cellar Traders

Leo Park
박 성민 (this is Korean character) on the English typying board: Leo Park
Managing Director

Suite 7/5 Harlow Rd
Bayfield WA 6923
Tel) +61(8) 6027 3518
Mob) +61(412) 305 276

leo.park@lumocellartraders.example
lumocellar@lumocellartraders.example
www.lumocellartraders.example

Target Market(s)

Asian Market

Industry/Entity Type

Business

Contact Information for Business Card

Lumo Cellar Traders

Leo Park
박 성민 (this is Korean character) English typying: Leo Park
Managing Director

Suite 7/5 Harlow Rd
Bayfield WA 6923
Tel) +61(8) 6027 3518
Mob) +61(412) 305 276

Font styles to use
Serif
Decorative

Colors
ec1f27
f78f21
f04a50
faa54b
cadf82
abd036

Requirements
Must have
• Company Logo & wine theme
Nice to have
• Very simple & modern
Should not have
• No Red Color on the name of Leo Park or 박 성민
• No traditional looking. young and modern look preferred

```html
<!DOCTYPE html>
<html lang="en">
<head>
<meta charset="utf-8">
<title>Lumo Cellar Traders – Business Card</title>
<link rel="stylesheet" href="https://fonts.googleapis.com/css2?family=Open+Sans:ital,wght@0,400;0,600;0,700;1,400&family=Noto+Sans+KR:wght@400;500&display=swap">
<style>
  :root {
    --backdrop: #4a423d;
    --card: #151515;
    --red: #d0202b;
    --wine: #a8243a;
    --gold: #c4923a;
    --white: #f2f2f2;
    --muted: #b9b9b9;
    --divider: #d8d8d8;
  }
  * { box-sizing: border-box; margin: 0; padding: 0; }
  html, body {
    width: 1200px; height: 864px; overflow: hidden;
    background: var(--backdrop);
    font-family: "Open Sans", Arial, sans-serif;
  }
  .canvas { position: relative; width: 1200px; height: 864px; }
  .card {
    position: absolute; width: 530px; height: 303px;
    background: var(--card);
    border-radius: 3px;
    box-shadow: 0 10px 28px rgba(0,0,0,.45);
  }
  .card--front { left: 50px; top: 150px; }
  .card--details { left: 620px; top: 410px; }

  /* front */
  .brand {
    position: absolute; left: 70px; top: 82px;
    display: flex; align-items: center; gap: 16px;
  }
  .brand__dot {
    width: 58px; height: 58px; border-radius: 50%;
    background: var(--wine);
  }
  .brand__name {
    font-weight: 700; font-size: 32px; line-height: 1.05;
    color: var(--wine); letter-spacing: .5px;
    text-transform: uppercase;
  }
  .tagline {
    position: absolute; left: 144px; top: 168px;
    font-size: 13px; font-style: italic; color: var(--gold);
  }
  .front-web {
    position: absolute; left: 70px; top: 236px;
    font-size: 13px; letter-spacing: 2.4px; color: var(--muted);
  }

  /* details */
  .mark {
    position: absolute; left: 34px; top: 112px; width: 180px;
    display: flex; flex-direction: column; align-items: center; gap: 10px;
  }
  .mark__dot { width: 46px; height: 46px; border-radius: 50%; background: var(--wine); }
  .mark__name {
    font-weight: 700; font-size: 17px; color: var(--wine);
    text-transform: uppercase; text-align: center; line-height: 1.15;
  }
  .divider {
    position: absolute; left: 232px; top: 40px; width: 1px; height: 222px;
    background: linear-gradient(var(--card), var(--divider) 30%, var(--divider) 70%, var(--card));
  }
  .person { position: absolute; left: 252px; top: 40px; right: 16px; }
  .person__name { font-weight: 700; font-size: 13px; color: var(--white); letter-spacing: .5px; line-height: 16px; text-transform: uppercase; }
  .person__role { font-size: 14px; color: var(--gold); letter-spacing: .5px; line-height: 17px; }
  .person__korean { font-family: "Noto Sans KR", sans-serif; font-size: 14px; color: var(--gold); line-height: 19px; }
  .address { margin-top: 8px; font-size: 13px; line-height: 17px; color: var(--white); }
  .contacts { list-style: none; margin-top: 4px; }
  .contacts li {
    display: flex; align-items: center; gap: 8px;
    font-size: 13px; line-height: 17px; color: var(--white);
    white-space: nowrap;
  }
  .icon { width: 11px; height: 11px; flex: none; fill: var(--red); }
</style>
</head>
<body>
<main class="canvas">

  <section class="card card--front" aria-label="Card front">
    <div class="brand">
      <span class="brand__dot"></span>
      <span class="brand__name">Lumo Cellar<br>Traders</span>
    </div>
    <p class="tagline">Connect &amp; Develop Your Business</p>
    <p class="front-web">www.lumocellartraders.example</p>
  </section>

  <section class="card card--details" aria-label="Card details side">
    <div class="mark">
      <span class="mark__dot"></span>
      <span class="mark__name">Lumo Cellar Traders</span>
    </div>
    <div class="divider"></div>
    <div class="person">
      <p class="person__name">Leo Park</p>
      <p class="person__role">MANAGING DIRECTOR</p>
      <p class="person__korean">박 성민</p>
      <p class="address">Suite 7/5 Harlow Rd<br>Bayfield WA 6923</p>
      <ul class="contacts">
        <li><svg class="icon" viewBox="0 0 12 12"><path d="M1 3.5C1 2 2 1 3 1h6c1 0 2 1 2 2.5H8.5V2.8h-5v.7zM2 5h8l1 6H1z"/></svg>+61(8) 6027 3518</li>
        <li><svg class="icon" viewBox="0 0 12 12"><path d="M3 0h6v12H3zM4 1.5v8h4v-8z"/></svg>+61(412) 305 276</li>
        <li><svg class="icon" viewBox="0 0 12 12"><path d="M0 2h12v1.2L6 7 0 3.2zM0 4.6l6 3.8 6-3.8V10H0z"/></svg>leo.park@lumocellartraders.example</li>
        <li><svg class="icon" viewBox="0 0 12 12"><path d="M0 2h12v1.2L6 7 0 3.2zM0 4.6l6 3.8 6-3.8V10H0z"/></svg>lumocellar@lumocellartraders.example</li>
        <li><svg class="icon" viewBox="0 0 12 12"><circle cx="6" cy="6" r="5.5"/><path d="M.5 6h11M6 .5c-2.5 3-2.5 8 0 11M6 .5c2.5 3 2.5 8 0 11" stroke="#151515" stroke-width="1" fill="none"/></svg>www.lumocellartraders.example</li>
      </ul>
    </div>
  </section>

</main>
</body>
</html>
```